Business Card Design for LeafSpire (Farming Devices)

We need Business Cards for our new Company based in Switzerland called "LeafSpire" We develop innovativ products for indoor and outdoor Farming for household and components for vertical farming. Our initial BloomNook gives people the possibility to grow their own food at home all year round. The design should communicate freshness, innovation, health.

```html
<!DOCTYPE html>
<html lang="en">
<head>
<meta charset="utf-8">
<title>LeafSpire Business Card</title>
<link href="https://fonts.googleapis.com/css2?family=Poppins:wght@400;500;600;700&display=swap" rel="stylesheet">
<style>
  :root {
    --page-bg: #e9ebec;
    --brand-blue: #1470b8;
    --brand-blue-deep: #0f69b4;
    --brand-green: #6db43f;
    --brand-green-light: #7cbc3f;
    --white: #ffffff;
    --card-shadow: 0 18px 40px rgba(0,0,0,0.18);
  }
  * { margin: 0; padding: 0; box-sizing: border-box; }
  html, body {
    width: 1200px; height: 1108px; overflow: hidden;
    background: var(--page-bg);
    font-family: "Poppins", sans-serif;
  }
  .stage {
    position: relative; width: 1200px; height: 1108px;
    display: flex; justify-content: center; align-items: center; gap: 60px;
  }
  .card {
    position: relative; width: 420px; height: 700px;
    border-radius: 22px; overflow: hidden; box-shadow: var(--card-shadow);
  }
  /* Front */
  .card-front {
    background: linear-gradient(180deg, var(--brand-blue) 0%, #3d8a96 45%, var(--brand-green-light) 100%);
    display: flex; justify-content: center; align-items: center;
  }
  .front-wordmark {
    color: var(--white); font-weight: 600; font-size: 50px; letter-spacing: 0.5px;
    margin-top: -40px;
  }
  /* Back */
  .card-back { background: var(--white); }
  .back-wordmark {
    position: absolute; top: 150px; left: 0; right: 0; text-align: center;
    color: var(--brand-blue); font-weight: 600; font-size: 52px; letter-spacing: 0.5px;
  }
  .back-wave { position: absolute; left: 0; top: 300px; width: 420px; height: 400px; }
  .contact {
    position: absolute; top: 390px; left: 0; right: 0; text-align: center; color: var(--white);
  }
  .contact-name { font-weight: 700; font-size: 30px; line-height: 1.1; }
  .contact-role { color: var(--brand-green-light); font-weight: 500; font-size: 19px; margin-top: 2px; }
  .icon-row { display: flex; justify-content: center; gap: 8px; margin: 14px 0 6px; }
  .icon { width: 20px; height: 20px; }
  .contact-line { font-size: 17px; line-height: 1.45; font-weight: 400; }
  .address { margin-top: 4px; }
</style>
</head>
<body>
<main class="stage">
  <section class="card card-front" aria-label="Card front">
    <div class="front-wordmark">LeafSpire</div>
  </section>

  <section class="card card-back" aria-label="Card back">
    <div class="back-wordmark">LeafSpire</div>
    <svg class="back-wave" viewBox="0 0 420 400" preserveAspectRatio="none" aria-hidden="true">
      <path d="M0 70 C 90 10, 230 -10, 420 30 L420 400 L0 400 Z" fill="var(--brand-green)"/>
      <path d="M0 88 C 100 30, 240 10, 420 44 L420 400 L0 400 Z" fill="var(--brand-blue-deep)"/>
    </svg>
    <div class="contact">
      <div class="contact-name">Lena Hartmann</div>
      <div class="contact-role">Initiator &amp; Co-Founder</div>
      <div class="icon-row">
        <svg class="icon" viewBox="0 0 20 20" aria-label="Phone"><circle cx="10" cy="10" r="10" fill="var(--brand-green)"/><path d="M7 5.5l1.6 2.3-1 1c.6 1.3 1.4 2.1 2.6 2.6l1-1 2.3 1.6-.8 1.6c-3.4-.3-6.3-3.2-6.5-6.6z" fill="#fff"/></svg>
        <svg class="icon" viewBox="0 0 20 20" aria-label="Email"><circle cx="10" cy="10" r="10" fill="var(--brand-green)"/><rect x="5.5" y="6.5" width="9" height="7" rx="1" fill="#fff"/><path d="M5.8 7l4.2 3.3L14.2 7" stroke="var(--brand-green)" stroke-width="1" fill="none"/></svg>
        <svg class="icon" viewBox="0 0 20 20" aria-label="Website"><circle cx="10" cy="10" r="10" fill="var(--brand-green)"/><circle cx="10" cy="10" r="4.6" stroke="#fff" stroke-width="1.1" fill="none"/><path d="M5.4 10h9.2M10 5.4c-2 2.6-2 6.6 0 9.2M10 5.4c2 2.6 2 6.6 0 9.2" stroke="#fff" stroke-width="1" fill="none"/></svg>
      </div>
      <div class="contact-line">+41 79 210 48 36</div>
      <div class="contact-line">lena.hartmann@leafspire.ch</div>
      <div class="contact-line">www.leafspire.ch</div>
      <div class="icon-row">
        <svg class="icon" viewBox="0 0 20 20" aria-label="Location"><circle cx="10" cy="10" r="10" fill="var(--brand-green)"/><path d="M10 4.5a3.5 3.5 0 0 0-3.5 3.5c0 2.6 3.5 7 3.5 7s3.5-4.4 3.5-7A3.5 3.5 0 0 0 10 4.5z" fill="#fff"/><circle cx="10" cy="8" r="1.3" fill="var(--brand-green)"/></svg>
      </div>
      <div class="contact-line address">Seeweg 14</div>
      <div class="contact-line">CH-9400 Rorschach</div>
    </div>
  </section>
</main>
</body>
</html>
```